Snapnook needs You

Help us create an inviting, amazing, sleek, simple, clear landing page for a picture-memory-social connection site!

Business Name: SnapNook
Industry: Social Networking and Creativity through Pictures
A web platform for and about a community that is driven by a passion for sharing, caring, bonding, collaborating, creating and earning with pictures, through pictures and other related creative activities. This is going to be a great site for all creative artists-photographers, artists, graphic artists to express their work and their creativity.

The main focus of the site is - CONNECTIONS.
This will be uncoded.

Desired Website Screen Size
1024x768... Widescreen/Landscape orientation, is what we mean... So it fits on a CPU screen.

Desired look and feel and message
Look: Visitor should feel immersed in the page, in the world the page creates, simple, elegant, sophisticated, contemporary. We really like a clean uncluttered look.

Special mention: By the way we love the marketing genius who thought up this branding for velu yogurt where they used the two dots above the o to create a branding effect that made this brand instantly identifiable. http://www.velu-dairy.ca/en/

The two dots by themselves without having even the name present brings up the whole brand now. The dots are used above all the ingredients of the yogurt creating friendly figures, and above people in commercials-bringing the people onto the side of "team" velu. Snapnook may have a character created or something distinctive in the letters in the name created to brand the site as well.

Feel: Engaging; Magical without being corny, here is a link to give an example look and feel but please do not be hindered in your creativity by this suggestion. We love all creative angles.
http://artscrapheap.com/graphic/5820317-camera-film-roll-blue-background

Message: Life and memories and connections through pictures.

Target audience:
The site is focused on pictures but not confined to photography enthusiasts (although they are an integral part of the site). Customers/Visitors will include families, corporates and the younger generation - all age groups, all class, everyone with pictures to express, memories to share.

Website design we like:
http://morvantstudio.com/work/northern-ballet-guild/
http://morvantstudio.com/work/pixelhop/

What colors do we want to see on our landing page?
We would like the background to be grey or blue since it is grey is picture neutral colour and blue highlights pictures well and we also like blue and silver, which can be integrated into the theme. Also like green. But please do not let these instructions limit your creativity. We are open to new ideas and colours.

Predetermined Concepts if any:
We have a concept in mind and we think it would be cool to have an interface for the user through the back of a camera on the landing page -This could be used to create a scene or world the visitor feels a part of or is immersed into. The back screen of the camera may act as a screen for the slideshow of featured pictures on the site.

Content on the Page:
Photo Gallery with full screen, thumbnail view, zoom option etc.
Prominent but short introductory message
Sign in / Login Options
Links: Home Page; About; Info/Help; Contact Us; Privacy Policy; Terms of Use
At the bottom of the page: Follow Me/Like/Workfolio...social buttons.

Please feel free to add any other element to the landing page that you think might add to the effect of simple yet amazing look -clean, simple, uncluttered, sophisticated, stylish, inviting and engaging.
The concept is a guideline, but we would like you to be as creative as you can, even if it meant stepping out of these guidelines - rethink design, style, content if you like. We believe in bringing a solution in an innovative yet simple and elegant style. Something a visitor would be intrigued enough to explore and the guest would feel comfortable enough taking that step forward to have fun on the site. If you believe in the same, and you have the skill then you will have what we need. Good luck, go for it and we are excited to see what the amazing designers on this amazing site have to offer.
If you have any questions please free to ask.
Updates

HI wanted to send an update that this project design has been guaranteed.

Our site will be one to celebrate and showcase imagination as well as connection.  We would love to see what you create. Keep in mind our site will showcase all creativity, photographs, artists, graphic artists so this would be a benefit you may want to take advantage of in the future, a place where, if you so choose, you could gain exposure for your work. Therefore, even if you do not win the design project there is possible future benefit.

Imagination is everything.
Imagination encircles the world.-Harwood

Reason: We are giving the designers who accepted invites but have not yet submitted a chance to finish their submissions and the ones who are working on revisions a chance to finish those:)

Hello everyone,

Due to time constraints we must come to a decision sooner than the deadline of 28th. 

So, please try to submit any new designs or modifications to the old ones before the 26th. We are very thankful to all of you who have participated - for your designs, enthusiasm and kind words. 

Good luck! :)

• Thank you for the interest shown and your submissions! Designers who have submitted up until now have shown great potential. We are VERY excited with the quality of work and designs.

We want to add that Snapnook is not exclusively for the photographers. The site is for every person who may have a picture to store, organise, use or share - whether publicly or with only a few friends and family.

Snapnook is about allowing people to take control of their creativity. It is about providing tools to our users so that they can build their own connections and social network... of friends, family, fans, clients, ideas, thoughts, emotions etc. through pictures without worrying about their privacy or control over their creations.

With this update we want to encourage others to go beyond the camera theme. Do not let us restrict your creativity. Let YOUR OWN ideas take over if that’s what you think will best convey the message and will appeal to the users.

```html
<!DOCTYPE html>
<html lang="en">
<head>
<meta charset="utf-8">
<title>SnapNook — Welcome</title>
<link rel="stylesheet" href="https://fonts.googleapis.com/css2?family=Arimo:wght@400;700&family=Gochi+Hand&family=Kalam:wght@400&display=swap">
<style>
  :root {
    --bg: #0b0b0b;
    --bg-glow: #242424;
    --text: #ffffff;
    --text-soft: #cfcfcf;
    --text-muted: #9a9a9a;
    --text-faint: #555555;
    --bar: #1d1d1d;
    --panel-edge: #3c3c3c;
    --panel: #2a2a2a;
    --thumb-frame: #0d0d0d;
    --blue-top: #3bbbe8;
    --blue-bottom: #1690c8;
    --grey-top: #5a5a5a;
    --grey-bottom: #2e2e2e;
    --polaroid: #f4f4f4;
    --caption: #555555;
  }
  * { box-sizing: border-box; margin: 0; padding: 0; }
  html, body { width: 1200px; height: 939px; overflow: hidden; background: var(--bg); }
  body { font-family: "Arimo", Arial, sans-serif; color: var(--text); }

  .page {
    position: relative;
    width: 1150px; height: 900px;
    transform: scale(1.04348);
    transform-origin: 0 0;
    background:
      radial-gradient(ellipse 700px 420px at 560px 120px, var(--bg-glow), transparent 70%),
      var(--bg);
  }

  .brand {
    position: absolute; left: 88px; top: 36px;
    font-size: 52px; font-weight: 700; letter-spacing: -1px;
    color: #eeeeee;
  }

  .account-bar {
    position: absolute; left: 580px; top: 44px; width: 485px; height: 41px;
    background: linear-gradient(90deg, transparent, var(--bar) 30%);
    display: flex; align-items: center; justify-content: flex-end;
    padding-right: 19px; gap: 14px;
    font-size: 12px; color: #e4e4e4;
  }

  .side-nav {
    position: absolute; left: 88px; top: 117px; width: 154px; height: 260px;
    border-left: 2px solid #3a3a3a;
    list-style: none;
  }
  .side-nav li {
    position: absolute; left: 0; width: 154px; height: 23px;
    padding-left: 19px; line-height: 23px;
    font-size: 12.5px; color: var(--text-muted);
  }
  .side-nav li.is-active { background: var(--bar); color: var(--text); }
  .side-nav li.is-active::before {
    content: ""; position: absolute; left: -2px; top: 5px;
    border-left: 7px solid #6a6a6a;
    border-top: 6px solid transparent; border-bottom: 6px solid transparent;
  }

  .gallery {
    position: absolute; left: 286px; top: 126px; width: 779px; height: 255px;
    background: linear-gradient(#303030, #262626);
    border: 5px solid var(--panel-edge);
    box-shadow: 0 4px 10px rgba(0,0,0,.7);
  }
  .thumb {
    position: absolute; width: 123px; height: 99px;
    border: 4px solid var(--thumb-frame);
    box-shadow: 0 1px 3px rgba(0,0,0,.6);
  }
  .gallery-arrow {
    position: absolute; top: 101px; width: 44px; height: 44px;
    border-radius: 50%; background: linear-gradient(#444, #2c2c2c);
    box-shadow: inset 0 1px 0 #555, 0 1px 3px rgba(0,0,0,.6);
  }
  .tooltip {
    position: absolute; left: 88px; top: 116px; width: 162px; height: 33px;
    background: #141414; border: 1px solid #3a3a3a; border-radius: 3px;
    font-size: 12px; color: #d8d8d8; line-height: 31px; text-align: center;
    box-shadow: 0 2px 6px rgba(0,0,0,.7);
  }
  .tooltip::before {
    content: ""; position: absolute; left: 74px; top: -7px;
    border-bottom: 7px solid #141414;
    border-left: 7px solid transparent; border-right: 7px solid transparent;
  }

  .hero-photo {
    position: absolute; left: 70px; top: 410px; width: 560px; height: 455px;
    background:
      radial-gradient(circle 70px at 415px 650px, #6a6a6a, transparent),
      radial-gradient(circle 45px at 580px 530px, #4a4a4a, transparent),
      radial-gradient(circle 40px at 540px 600px, #3e3e3e, transparent),
      linear-gradient(100deg, #1c1c1c 0%, #3a3a3a 40%, #2a2a2a 65%, #121212 100%);
    background-position: -70px -410px, -70px -410px, -70px -410px, 0 0;
    background-size: 1150px 900px, 1150px 900px, 1150px 900px, 100% 100%;
    background-repeat: no-repeat;
    -webkit-mask-image: radial-gradient(ellipse 290px 240px at 280px 230px, #000 55%, transparent 100%);
    mask-image: radial-gradient(ellipse 290px 240px at 280px 230px, #000 55%, transparent 100%);
  }

  .welcome { position: absolute; left: 616px; top: 420px; width: 450px; }
  .welcome h1 { font-weight: 400; font-size: 24px; margin-left: 3px; margin-bottom: 17px; }
  .welcome p {
    font-size: 12px; line-height: 22px; color: var(--text-soft); text-align: justify;
  }

  .btn {
    position: absolute; top: 564px; width: 212px; height: 53px;
    border-radius: 3px;
    display: flex; align-items: center; justify-content: center; gap: 12px;
    font-size: 22px; font-weight: 700; color: var(--text);
    text-shadow: 0 1px 1px rgba(0,0,0,.4);
  }
  .btn-signin { left: 616px; background: linear-gradient(var(--blue-top), var(--blue-bottom)); }
  .btn-register { left: 847px; background: linear-gradient(var(--grey-top), var(--grey-bottom)); }

  .tagline {
    position: absolute; left: 620px; top: 644px; width: 445px;
    display: flex; justify-content: space-between;
    font-family: "Gochi Hand", cursive; font-size: 19px; color: var(--text-faint);
  }

  .polaroid {
    position: absolute; width: 116px; height: 138px;
    background: linear-gradient(#fafafa, #e6e6e6);
    padding: 8px 8px 24px;
    box-shadow: 0 3px 8px rgba(0,0,0,.6);
  }
  .polaroid .shot { width: 100%; height: 100%; }
  .polaroid .caption {
    position: absolute; right: 10px; bottom: 4px;
    font-family: "Kalam", cursive; font-size: 9px; color: var(--caption);
  }

  .footer {
    position: absolute; left: 0; top: 873px; width: 1150px;
    text-align: center; font-size: 12px; color: var(--text-muted);
  }
</style>
</head>
<body>
<div class="page">
  <div class="brand">SnapNook</div>

  <nav class="account-bar"><span>LOG IN</span><span>|</span><span>LOG OUT</span></nav>

  <ul class="side-nav">
    <li class="is-active" style="top:13px">HOME</li>
    <li style="top:53px">ABOUT US</li>
    <li style="top:93px">CONTACT US</li>
    <li style="top:133px">HELP</li>
    <li style="top:173px">PRIVACY POLICY</li>
    <li style="top:213px">TERMS OF USE</li>
  </ul>

  <section class="gallery">
    <div class="gallery-arrow" style="left:1px">
      <svg width="44" height="44"><path d="M23 14 L15 22 L23 30 Z" fill="#111"/></svg>
    </div>
    <div class="gallery-arrow" style="left:724px">
      <svg width="44" height="44"><path d="M21 14 L29 22 L21 30 Z" fill="#2f7fe0"/></svg>
    </div>

    <div class="thumb" role="img" aria-label="Featured photo: splashing bottle" style="left:55px;top:17px;background:radial-gradient(circle at 35% 45%,#b8a080,#3a1018 35%,#6a1420 70%,#1a0508)"></div>
    <div class="thumb" role="img" aria-label="Featured photo: hand and soap bubble" style="left:189px;top:17px;background:radial-gradient(circle at 70% 40%,#c8d890,#7a9a30 50%,#3a5a10)"></div>
    <div class="thumb" role="img" aria-label="Featured photo: black and white child portrait" style="left:323px;top:17px;background:radial-gradient(circle at 50% 60%,#e8e8e8,#9a9a9a 50%,#3a3a3a)"></div>
    <div class="thumb" role="img" aria-label="Featured photo: diver under stormy sky" style="left:457px;top:17px;background:linear-gradient(#5a7a8a,#a8c8d4 45%,#3a8a9a 75%,#1a5060)"></div>
    <div class="thumb" role="img" aria-label="Featured photo: fire portrait" style="left:591px;top:17px;background:radial-gradient(circle at 60% 50%,#ffd060,#e07010 45%,#5a1a02)"></div>

    <div class="thumb" role="img" aria-label="Featured photo: blossoming branch" style="left:55px;top:128px;background:radial-gradient(circle at 40% 40%,#d8dcc8,#8a9a80 55%,#3a4a30)"></div>
    <div class="thumb" role="img" aria-label="Featured photo: bokeh lights" style="left:189px;top:128px;background:radial-gradient(circle at 30% 35%,#f0c060,#a06020 40%,#2a3a20 80%)"></div>
    <div class="thumb" role="img" aria-label="Featured photo: autumn tree" style="left:323px;top:128px;background:linear-gradient(#e8d0c0,#a87a60 55%,#c8a080 75%,#6a4a30)"></div>
    <div class="thumb" role="img" aria-label="Featured photo: bird in flight" style="left:457px;top:128px;background:linear-gradient(#8aa8c8,#c0b0a0 55%,#d89050)"></div>
    <div class="thumb" role="img" aria-label="Featured photo: portrait among leaves" style="left:591px;top:128px;background:radial-gradient(circle at 65% 50%,#c8c0b0,#5a7a40 45%,#1a3010)"></div>

    <div class="tooltip">Bottle by&nbsp; Mara Linden</div>
  </section>

  <div class="hero-photo" role="img" aria-label="Vintage folding camera in soft black and white light with bokeh"></div>

  <section class="welcome">
    <h1>Welcome to our site</h1>
    <p>At vero eos et accusamus et iusto odio dignissimos ducimus qui blanditiis praesen tium voluptatum deleniti atque corrupti quos dolores et quas molestias excepturi sint occaecati cupiditate non provident, similique sunt in culpa qui officia.</p>
  </section>

  <a class="btn btn-signin">SIGN IN
    <svg width="16" height="16"><circle cx="8" cy="8" r="8" fill="#1a2a33"/><path d="M4 8h6M8 5l3 3-3 3" stroke="#fff" stroke-width="1.6" fill="none"/></svg>
  </a>
  <a class="btn btn-register">REGISTER
    <svg width="16" height="16"><circle cx="8" cy="8" r="8" fill="#111"/><path d="M4 8h6M8 5l3 3-3 3" stroke="#fff" stroke-width="1.6" fill="none"/></svg>
  </a>

  <div class="tagline"><span>join with us....</span><span>Meet New People....</span><span>Share New things</span></div>

  <div class="polaroid" style="left:629px;top:688px;transform:rotate(-3deg)">
    <div class="shot" role="img" aria-label="Member photo: young man" style="background:radial-gradient(circle at 50% 45%,#e0c0a8,#a8c0d0 45%,#7890a0)"></div>
    <span class="caption">Ivo Brandt</span>
  </div>
  <div class="polaroid" style="left:722px;top:694px;transform:rotate(-11deg)">
    <div class="shot" role="img" aria-label="Member photo: photographer with camera" style="background:radial-gradient(circle at 45% 50%,#303030,#8a8a8a 35%,#e8eef2 70%)"></div>
    <span class="caption">Ivo Brandt</span>
  </div>
  <div class="polaroid" style="left:806px;top:690px;width:124px;height:144px;transform:rotate(9deg)">
    <div class="shot" role="img" aria-label="Member photo: photographer with camera" style="background:radial-gradient(circle at 40% 40%,#202020,#d0a890 35%,#88a8b8 70%)"></div>
    <span class="caption">Ivo Brandt</span>
  </div>
  <div class="polaroid" style="left:910px;top:690px;width:104px;transform:rotate(14deg)">
    <div class="shot" role="img" aria-label="Member photo: smiling woman" style="background:radial-gradient(circle at 50% 45%,#c8987a,#4a3a30 40%,#c8d0d4 75%)"></div>
    <span class="caption">Ivo Brandt</span>
  </div>

  <footer class="footer">Copyright © 2012 www.snapnook.com &nbsp;&nbsp; All rights reserved.</footer>
</div>
</body>
</html>
```